The Maplewood Family Clinic needs a Letterhead

We are a bilingual pediatric clinic located in Montreal, Canada.

Our english name is Maplewood Family Clinic
Our french name is Clinique du parc Verdelle

We offer complete care for children including general pediatric care, pediatric specialist care such as Ear, Nose and Throat, Urology, Neurology and Adolescent Medicine. We also have paramedical specialists such as psychologists, social workers, occupational therapists, speech and language pathologists.

The letterhead must use and be harmonious with our new logo. See Design #7150846. We need two types of letterhead. One for a the Logo and both english and french names on the top and the second with the list of current staff on the left. I have uploaded two old examples for you to see. Thanks and good luck.

Industry/Entity Type

Clinic

Font styles to use
Sans Serif

Colors
3176b5
9d9d9d

Requirements
Must have
• Include our logo.
Nice to have
• Most of our printing is done in black and white. So a grayscale design is fine.
I have included a color and grayscale versions of our logo.

We prefer clean modern designs.

```html
<!DOCTYPE html>
<html lang="fr">
<head>
<meta charset="utf-8">
<title>Maplewood Family Clinic – Letterhead</title>
<link rel="stylesheet" href="https://fonts.googleapis.com/css2?family=Arimo:wght@400;700&display=swap">
<style>
  :root {
    --brand: #5a60ad;
    --label: #3f55b0;
    --grey: #9d9d9d;
    --rule: #3176b5;
    --paper: #ffffff;
    --emblem-tint: #ecebf1;
    --emblem-fade: rgba(236, 235, 241, 0);
  }
  html, body { margin: 0; padding: 0; overflow: hidden; background: var(--paper); }
  .letterhead {
    position: relative;
    width: 849px;
    height: 1200px;
    overflow: hidden;
    background: var(--paper);
    font-family: "Arimo", Arial, sans-serif;
  }
  .emblem-area {
    position: absolute;
    left: 0;
    top: 580px;
    width: 745px;
    height: 520px;
    background: radial-gradient(ellipse at 50% 55%, var(--emblem-tint) 0%, var(--emblem-tint) 45%, var(--emblem-fade) 80%);
  }
  .brand {
    position: absolute;
    top: 40px;
    right: 48px;
    display: flex;
    align-items: center;
    gap: 14px;
    color: var(--brand);
    font-size: 17px;
    line-height: 19px;
  }
  .brand-name { margin: 0; font-weight: 400; font-size: 17px; }
  .brand-name--fr { text-align: right; }
  .brand-name--en { text-align: left; }
  .brand-dot {
    width: 14px; height: 14px; border-radius: 50%;
    background: var(--brand);
  }
  .footer {
    position: absolute;
    left: 14px;
    top: 1117px;
    display: flex;
    font-size: 11px;
    line-height: 11.6px;
    color: var(--grey);
  }
  .footer-address { width: 238px; }
  .footer-rule {
    width: 1px;
    height: 58px;
    background: var(--rule);
    margin-right: 24px;
  }
  .label { color: var(--label); }
  .footer p { margin: 0; white-space: nowrap; }
</style>
</head>
<body>
<div class="letterhead">
  <div class="emblem-area" role="img" aria-label="Large faint clinic emblem in the background"></div>

  <header class="brand">
    <p class="brand-name brand-name--fr">Clinique<br>du parc<br>Verdelle</p>
    <span class="brand-dot"></span>
    <p class="brand-name brand-name--en">Maplewood<br>Family<br>Clinic</p>
  </header>

  <footer class="footer">
    <div class="footer-address">
      <p class="label">Addresse / Address</p>
      <p>2380 boul. des Érables, Suite 210</p>
      <p>Verdelle, Qc H8R 2L5</p>
      <p>Tél. (514) 555-0148 | Fax. (514) 555-0193</p>
    </div>
    <div class="footer-rule"></div>
    <div class="footer-staff">
      <p><span class="label">Pédiatres / Pediatricians:</span> A. Bellamy, P. Corriveau, L. Dufresne, M. Garand, S. Lachance, E. Marlowe, J. Talbot</p>
      <p><span class="label">Neurologue / Neurologist:</span> K. Renaud &nbsp;<span class="label">O.R.L. / E.N.T.:</span> F. Naser &nbsp;<span class="label">Urologue / Urologist:</span> B. Olsen</p>
      <p><span class="label">Psychologues / Psychologists:</span> C. Fortier, G. Hébert &nbsp;<span class="label">Travailleuse social / Social worker:</span> V. Lenoir</p>
      <p><span class="label">Dietetiste / Dietician:</span> D. Arsenault &nbsp;<span class="label">Gerante / Manager:</span> R. Castell</p>
    </div>
  </footer>
</div>
</body>
</html>
```